Need a sleek, professional business card design for a Web Development business

I need a unique business card designed for a web development company. It is also the parent company for any ventures I do, such as my ClipWave channel, startup ideas I have, etc. I am the single member of "Bright Harbor Code LLC." I will attach my basic logo here, so you will see the current color scheme and have the asset available. Thank you!

Target Market(s)

Startups, SMB's, Professionals

Industry/Entity Type

Business

Font styles to use
Other font styles liked:
• Lovello for headings is what I use, but not necessary.

Colors

Designer to choose colors to be used in the design.

Requirements
Nice to have
• Sleek is the word. Professional, modern, dark.
Should not have
• Any work from someone else's design. Lacking originality.

```html
<!DOCTYPE html>
<html lang="en">
<head>
<meta charset="UTF-8">
<title>Bright Harbor Code LLC — Business Card</title>
<link rel="stylesheet" href="https://fonts.googleapis.com/css2?family=Montserrat:wght@500;700&family=Josefin+Sans:wght@700&display=swap">
<style>
  :root {
    --page-bg: #efedea;
    --card-peach: #f9a764;
    --card-coral: #f2706f;
    --card-dark: #222222;
    --text-amber: #f6a35e;
    --brand-rose: #f0686f;
  }
  * { margin: 0; padding: 0; box-sizing: border-box; }
  html, body {
    width: 1200px;
    height: 863px;
    overflow: hidden;
    background: var(--page-bg);
  }
  .business-card {
    position: absolute;
    left: 430px;
    top: 134px;
    width: 340px;
    height: 595px;
    border-radius: 4px;
    overflow: hidden;
    box-shadow: 0 10px 30px rgba(0,0,0,0.15);
    background: var(--card-dark);
  }
  .card-artwork {
    position: absolute;
    inset: 0;
    background:
      radial-gradient(ellipse 78% 58% at 50% 50%,
        var(--card-dark) 0%,
        var(--card-dark) 62%,
        rgba(34,34,34,0) 100%),
      linear-gradient(180deg, var(--card-peach) 0%, var(--card-coral) 100%);
  }
  .card-content {
    position: absolute;
    inset: 0;
    text-align: center;
    color: var(--text-amber);
    font-family: "Montserrat", sans-serif;
  }
  .brand {
    position: absolute;
    top: 150px;
    left: 0;
    right: 0;
    display: flex;
    justify-content: center;
    align-items: center;
    gap: 12px;
  }
  .brand-mark {
    width: 30px;
    height: 30px;
    background: var(--brand-rose);
    border-radius: 4px;
  }
  .brand-name {
    font-family: "Josefin Sans", sans-serif;
    font-weight: 700;
    font-size: 15px;
    line-height: 1.15;
    letter-spacing: 0.5px;
    text-transform: uppercase;
    color: var(--brand-rose);
    text-align: left;
  }
  .person {
    position: absolute;
    top: 238px;
    left: 0;
    right: 0;
  }
  .person-name {
    font-family: "Josefin Sans", sans-serif;
    font-weight: 700;
    font-size: 21px;
    letter-spacing: 0.5px;
  }
  .person-title {
    font-size: 15px;
    font-weight: 500;
    margin-top: 2px;
  }
  .contact {
    position: absolute;
    left: 0;
    right: 0;
    font-size: 13.5px;
    font-weight: 500;
    line-height: 1.3;
  }
  .contact-phones { top: 318px; }
  .contact-online { top: 372px; }
</style>
</head>
<body>
  <div class="business-card">
    <div class="card-artwork" role="img" aria-label="Decorative curved bands in dark grey over a peach-to-coral gradient"></div>

    <div class="card-content">
      <div class="brand">
        <span class="brand-mark"></span>
        <span class="brand-name">Bright Harbor<br>Code LLC</span>
      </div>

      <div class="person">
        <p class="person-name">LOREM IPSUM</p>
        <p class="person-title">President</p>
      </div>

      <div class="contact contact-phones">
        <p>Office 012.345.678</p>
        <p>Direct 987.654.321</p>
      </div>

      <div class="contact contact-online">
        <p>youremail@domain.com</p>
        <p>www.yoursite.com</p>
      </div>
    </div>
  </div>
</body>
</html>
```